Design Tweak needed for a current site

Design on top of an existing quiz funnel

Ideally we would like to tweak what we have already built here (moving elements, styles, adding simple elements etc): http://offers.plumrivetdeals.com/can-you-save-on-car-insurance

The flow:
1) User lands on the quiz page
2) User answers X questions and moves through the flow
3) Calculating user results screen
4) User reaches a success screen, and is subsequently redirected

Keys to the design:
1) We need to emphasize the quiz title as that will drive engagement. In this case, this is a quiz to see if you might be eligible to save money on car insurance.

2) At the end of the quiz we need to make it very, very clear that the user is eligible for savings and that in order to complete the process they are being redirected to another page where they need to fill out a form. It is critical that the design communicates this very clearly... We can count down the time left until redirect and we can use any order of elements to make this point. I think our current design does a very bad job of this.

3) We want to have a "calculating" step so that it seems like the page is working in the background

Goals of the design:
1) Polished, high quality experience throughout
2) User is clearly prepared to be redirected to the conversion funnel/landing page at the end
3) User understands the value of completing the quiz

Target Market(s)

designers

Industry/Entity Type

Moving

Number of Pages Required

1 page

Font styles to use
Sans Serif

Colors

Designer to choose colors to be used in the design.

Requirements
Must have
• This quiz funnel is a template so while the current use case is for auto insurance, we would like a design that also would work in other contexts.
Should not have
• We don't want to materially change the core functionality of the quiz itself... redesigning any of the elements or interactions is encouraged though

```html
<!DOCTYPE html>
<html lang="en">
<head>
<meta charset="utf-8">
<title>PlumRivet Deals – Calculating your savings</title>
<link href="https://fonts.googleapis.com/css2?family=Jost:wght@300;400;500;600;700&display=swap" rel="stylesheet">
<style>
  :root {
    --header-blue: #1f6be8;
    --page-navy: #082d6f;
    --navy-deep: #06265f;
    --accent-yellow: #ffd60a;
    --ring-blue: #1a57c8;
    --dot-blue: #2a4f94;
    --white: #ffffff;
    --muted-label: #5d93f0;
    --divider: #4b8af0;
    --tick-green: #2ecc40;
  }
  * { box-sizing: border-box; margin: 0; padding: 0; }
  html, body { width: 1200px; height: 824px; overflow: hidden; }
  body {
    font-family: "Jost", "Futura", sans-serif;
    background: var(--page-navy);
    color: var(--white);
    position: relative;
  }

  .backdrop {
    position: absolute; left: 0; top: 167px; width: 1200px; height: 657px;
    background: linear-gradient(180deg, var(--page-navy) 0%, var(--page-navy) 30%, var(--navy-deep) 100%);
  }

  .site-header {
    position: absolute; left: 0; top: 0; width: 1200px; height: 167px;
    background: var(--header-blue);
  }
  .brand {
    position: absolute; left: 0; top: 36px; width: 1200px;
    display: flex; justify-content: center; align-items: center; gap: 10px;
  }
  .brand-dot {
    width: 30px; height: 30px; border-radius: 50%;
    border: 4px solid var(--white);
  }
  .brand-name { font-size: 30px; font-weight: 500; color: var(--white); letter-spacing: 0.3px; }

  .quiz-steps { position: absolute; left: 35px; top: 110px; width: 1128px; height: 57px; display: flex; }
  .step { flex: 1; position: relative; text-align: center; }
  .step-divider { position: absolute; bottom: 0; width: 1px; height: 20px; background: var(--divider); }
  .step-divider.is-start { left: 0; }
  .step-divider.is-end { right: 0; }
  .step-number {
    display: flex; justify-content: center; align-items: center; gap: 6px;
    font-size: 25px; font-weight: 700; line-height: 1; margin-top: 6px;
  }
  .step-label { font-size: 9.5px; font-weight: 600; color: var(--muted-label); margin-top: 6px; white-space: nowrap; }
  .step.is-current .step-label { color: var(--white); }
  .step.is-current::after {
    content: ""; position: absolute; left: 50%; margin-left: -18px; bottom: -3px;
    width: 36px; height: 5px; background: var(--accent-yellow);
  }
  .tick { width: 18px; height: 18px; }

  .calculating {
    position: absolute; left: 0; top: 280px; width: 1200px; text-align: center;
  }
  .calculating-title { font-size: 37px; font-weight: 700; line-height: 35px; letter-spacing: -0.3px; }

  .progress-dial { position: absolute; left: 507px; top: 405px; width: 182px; height: 182px; }
  .car-icon {
    position: absolute; left: 564px; top: 479px; width: 72px; height: 30px;
    border-radius: 12px 18px 6px 6px; background: var(--accent-yellow);
  }

  .status-note {
    position: absolute; left: 0; top: 616px; width: 1200px; text-align: center;
    font-size: 19.5px; font-weight: 300; letter-spacing: -0.2px;
  }
</style>
</head>
<body>
  <div class="backdrop" role="img" aria-label="Soft flowing wave decoration in deep navy tones"></div>

  <header class="site-header">
    <div class="brand">
      <span class="brand-dot"></span>
      <span class="brand-name">PlumRivet Deals</span>
    </div>

    <nav class="quiz-steps">
      <div class="step is-done">
        <span class="step-divider is-start"></span>
        <div class="step-number">
          <svg class="tick" viewBox="0 0 20 20" aria-hidden="true"><circle cx="10" cy="10" r="10" fill="var(--tick-green)"/><path d="M5.5 10.2l3 3 6-6.2" stroke="var(--page-navy)" stroke-width="2.4" fill="none" stroke-linecap="round" stroke-linejoin="round"/></svg>01
        </div>
        <div class="step-label">Do you lease or own?</div>
      </div>
      <div class="step is-current">
        <span class="step-divider is-start"></span>
        <div class="step-number">02</div>
        <div class="step-label">What kind of car do you drive</div>
      </div>
      <div class="step">
        <span class="step-divider is-start"></span>
        <div class="step-number">03</div>
        <div class="step-label">Do you currently have car insurance</div>
      </div>
      <div class="step">
        <span class="step-divider is-start"></span>
        <div class="step-number">04</div>
        <div class="step-label">Have you been in an accident...</div>
      </div>
      <div class="step">
        <span class="step-divider is-start"></span>
        <span class="step-divider is-end"></span>
        <div class="step-number">05</div>
        <div class="step-label">Final decision</div>
      </div>
    </nav>
  </header>

  <main>
    <section class="calculating">
      <h1 class="calculating-title">Calculating<br>your potentail savings...</h1>
    </section>

    <svg class="progress-dial" viewBox="0 0 182 182" aria-hidden="true">
      <circle cx="91" cy="91" r="90" fill="none" stroke="var(--white)" stroke-width="1.5" stroke-dasharray="5 4"/>
      <circle cx="91" cy="91" r="76" fill="none" stroke="var(--dot-blue)" stroke-width="4" stroke-dasharray="0 8.1" stroke-linecap="round"/>
      <circle cx="91" cy="91" r="64" fill="none" stroke="var(--ring-blue)" stroke-width="8"/>
      <circle cx="91" cy="91" r="64" fill="none" stroke="var(--accent-yellow)" stroke-width="8"
              stroke-dasharray="150 402" transform="rotate(-90 91 91)"/>
    </svg>
    <div class="car-icon" role="img" aria-label="Car icon"></div>

    <p class="status-note">Hang tight! We’re reviewing your answers and looking for savings</p>
  </main>
</body>
</html>
```